New Zealand Luggage Importer Needs Business Cards

We need professional, creative and fashionable business cards created.
We are based in New Zealand and import and distribute high-end, quality, fashionable and durable luggage.
We pride ourselves on selling the very best quality luggage, second only to 1 brand (which we won't mention here)...we use the same manufacturer. However, our prices are much more reasonable.
Industry/Entity Type
Business
Contact Information for Business Card
Mark Dunsley
027 512 4068
3/17 Harlow Street, Pinecrest Flats, Auckland, 0614
PO Box 204377, Fernside, Auckland 0731
09-528-3916
sales@brivancases.co.nz / www.brivancases.co.nz

```html
<!DOCTYPE html>
<html lang="en">
<head>
<meta charset="utf-8">
<title>Brivan Cases – Business Card</title>
<link rel="stylesheet" href="https://fonts.googleapis.com/css2?family=Source+Sans+3:wght@400;600;700&display=swap">
<style>
  :root {
    --paper: #ffffff;
    --card-black: #000000;
    --ink: #0d0d0d;
    --gold: #e3b55a;
    --gold-deep: #6d3c0c;
    --gold-light: #fbf3c8;
  }
  html, body {
    margin: 0;
    width: 1200px;
    height: 854px;
    overflow: hidden;
    background: var(--paper);
    font-family: "Source Sans 3", "Myriad Pro", sans-serif;
  }
  .canvas { position: relative; width: 1200px; height: 854px; }
  .card {
    position: absolute;
    width: 671px;
    height: 372px;
    background: var(--card-black);
    overflow: hidden;
    box-shadow: 6px 8px 14px rgba(0,0,0,0.35);
  }
  .card--front { left: 53px; top: 28px; }
  .card--back { left: 459px; top: 440px; }
  .card__art { position: absolute; inset: 0; width: 671px; height: 372px; }

  .holder-name {
    position: absolute;
    left: 51px;
    top: 48px;
    margin: 0;
    font-size: 62px;
    line-height: 1;
    color: var(--ink);
    font-weight: 400;
    letter-spacing: -1px;
  }
  .holder-name strong { font-weight: 700; }

  .contact-list {
    position: absolute;
    right: 42px;
    top: 198px;
    margin: 0;
    padding: 0;
    list-style: none;
  }
  .contact-list li {
    display: flex;
    justify-content: flex-end;
    align-items: center;
    height: 25.7px;
    font-size: 16px;
    color: var(--gold);
  }
  .contact-list svg { width: 18px; height: 18px; margin-left: 10px; flex: none; }

  .brand-name {
    position: absolute;
    left: 0;
    right: 0;
    top: 246px;
    margin: 0;
    text-align: center;
    font-size: 50px;
    font-weight: 600;
    letter-spacing: 4px;
    color: var(--gold);
  }
</style>
</head>
<body>
<div class="canvas">

  <section class="card card--front">
    <svg class="card__art" viewBox="0 0 671 372" aria-hidden="true">
      <defs>
        <linearGradient id="goldSweep" x1="0" y1="0" x2="1" y2="0">
          <stop offset="0" stop-color="#7a4510"/>
          <stop offset="0.25" stop-color="#e0b060"/>
          <stop offset="0.48" stop-color="#fbf3c8"/>
          <stop offset="0.75" stop-color="#d9a84e"/>
          <stop offset="1" stop-color="#6b3a0a"/>
        </linearGradient>
      </defs>
      <path class="gold-field" fill="url(#goldSweep)"
        d="M0 0 H671 V40 C560 34 470 62 360 120 C250 178 150 214 0 212 Z"/>
      <path class="gold-stripe" fill="url(#goldSweep)"
        d="M18 225 C170 228 290 175 400 128 C500 88 600 76 671 74 V92 C600 92 505 108 410 142 C300 184 190 226 18 225 Z"/>
    </svg>

    <h1 class="holder-name">Mark <strong>Dunsley</strong></h1>

    <ul class="contact-list">
      <li>027 512 4068; 09 528 3916
        <svg viewBox="0 0 18 18"><rect x="5" y="1" width="8" height="16" rx="1" fill="none" stroke="currentColor" stroke-width="1.4"/><rect x="6.5" y="3" width="5" height="5" fill="currentColor"/></svg>
      </li>
      <li>3/17 Harlow Street, Pinecrest Flats, Auckland, 0614
        <svg viewBox="0 0 18 18"><path d="M9 1 C5 1 3 4 3 7 C3 11 9 17 9 17 C9 17 15 11 15 7 C15 4 13 1 9 1 Z" fill="currentColor"/><circle cx="9" cy="7" r="2.4" fill="#000"/></svg>
      </li>
      <li>PO Box 204377, Fernside, Auckland 0731
        <svg viewBox="0 0 18 18"><rect x="1" y="4" width="16" height="10" fill="currentColor"/><path d="M1 4 L9 10 L17 4" fill="none" stroke="#000" stroke-width="1.2"/></svg>
      </li>
      <li>sales@brivancases.co.nz
        <svg viewBox="0 0 18 18"><circle cx="9" cy="9" r="3" fill="none" stroke="currentColor" stroke-width="1.8"/><path d="M12 6 V11 C12 13 16 13 16 9 A7 7 0 1 0 12.5 15" fill="none" stroke="currentColor" stroke-width="1.8"/></svg>
      </li>
      <li>www.brivancases.co.nz
        <svg viewBox="0 0 18 18" fill="none" stroke="currentColor" stroke-width="1"><circle cx="9" cy="9" r="7.5"/><ellipse cx="9" cy="9" rx="3.5" ry="7.5"/><path d="M1.5 9 H16.5 M3 5 H15 M3 13 H15"/></svg>
      </li>
    </ul>
  </section>

  <section class="card card--back">
    <svg class="card__art" viewBox="0 0 671 372" aria-hidden="true">
      <defs>
        <linearGradient id="goldSweepBack" x1="0" y1="0" x2="1" y2="0">
          <stop offset="0" stop-color="#7a4510"/>
          <stop offset="0.35" stop-color="#e0b060"/>
          <stop offset="0.6" stop-color="#fbf3c8"/>
          <stop offset="0.85" stop-color="#d9a84e"/>
          <stop offset="1" stop-color="#6b3a0a"/>
        </linearGradient>
      </defs>
      <path class="gold-stripe" fill="url(#goldSweepBack)"
        d="M15 194 C170 198 290 150 400 100 C500 55 600 30 671 28 V48 C600 46 505 70 410 112 C300 162 180 200 15 194 Z"/>
    </svg>
    <p class="brand-name">BRIVAN CASES</p>
  </section>

</div>
</body>
</html>
```